Dova Lenthe Christmas Card 2025

I need a Christmas card design for Dova Lenthe (www.dovalenthe.example). My client loves everything Mara Quillon. I’ve attached this year’s inspirations, including the live wreath she is gifting and the brand guidelines. She prefers the softer colors shown in the inspiration materials. The greeting should read Merry Christmas (not Happy Holidays). The final design should feel elegant, festive, and aligned with the Dova Lenthe brand.”

```html
<!DOCTYPE html>
<html lang="en">
<head>
<meta charset="utf-8">
<title>Dova Lenthe Christmas Card 2025</title>
<link rel="stylesheet" href="https://fonts.googleapis.com/css2?family=Montserrat:wght@300;400;500&display=swap">
<style>
  :root {
    --backdrop: #5f5f5f;
    --paper: #ffffff;
    --blush: #f3e0da;
    --orange: #f08a24;
    --brown: #4a2a22;
    --pine-soft: rgba(157, 181, 143, 0.28);
    --snow: #ffffff;
  }
  * { box-sizing: border-box; margin: 0; padding: 0; }
  html, body {
    width: 1200px; height: 1200px; overflow: hidden;
    background: var(--backdrop);
    font-family: "Montserrat", Arial, sans-serif;
  }
  .spread {
    position: absolute; left: 50px; top: 215px;
    width: 1100px; height: 770px;
    display: flex;
  }
  .panel {
    position: relative; width: 550px; height: 770px;
    background: var(--paper); overflow: hidden;
  }
  /* inside panel */
  .foliage-faded {
    position: absolute; border-radius: 50%;
    background: radial-gradient(circle, var(--pine-soft) 0%, rgba(157,181,143,0.12) 45%, rgba(255,255,255,0) 70%);
  }
  .foliage-faded.top-left { left: -120px; top: -60px; width: 380px; height: 380px; }
  .foliage-faded.bottom-right { left: 230px; top: 420px; width: 420px; height: 420px; }
  .brand-lockup {
    position: absolute; left: 191px; top: 356px;
    display: flex; align-items: center; gap: 14px;
  }
  .brand-dot {
    width: 60px; height: 60px; border-radius: 50%;
    background: var(--orange);
  }
  .brand-name {
    color: var(--brown); font-weight: 400;
    font-size: 23px; line-height: 1.15; letter-spacing: 3px;
    text-transform: uppercase;
  }
  /* cover panel */
  .cover-field {
    position: absolute; left: 17px; top: 19px; right: 17px; bottom: 19px;
    background: var(--blush);
  }
  .wreath {
    position: absolute; left: 50px; top: 40px;
    width: 465px; height: 465px; border-radius: 50%;
    background: radial-gradient(circle,
      rgba(240,138,36,0.9) 0%, rgba(240,138,36,0.85) 26%,
      rgba(120,150,100,0.75) 34%, rgba(157,181,143,0.55) 48%,
      rgba(157,181,143,0.18) 62%, rgba(243,224,218,0) 71%);
  }
  .greeting {
    position: absolute; left: 0; right: 0; top: 520px;
    text-align: center;
  }
  .greeting-year {
    color: var(--snow); font-weight: 500;
    font-size: 28px; letter-spacing: 9px; padding-left: 9px; line-height: 1;
  }
  .greeting-lead {
    margin-top: 12px;
    color: var(--brown); font-weight: 500;
    font-size: 10px; letter-spacing: 8px; padding-left: 8px;
    text-transform: uppercase;
  }
  .greeting-merry {
    margin-top: 10px;
    color: var(--orange); font-weight: 300;
    font-size: 40px; line-height: 1; letter-spacing: 1px;
  }
  .greeting-christmas {
    margin-top: 2px;
    color: var(--orange); font-weight: 300;
    font-size: 65px; line-height: 1; letter-spacing: 1px;
  }
</style>
</head>
<body>
  <main class="spread">
    <section class="panel panel-inside">
      <div class="foliage-faded top-left" role="img" aria-label="Faded snowy pine branch with pinecones and red berries, with thin looping line ornaments"></div>
      <div class="foliage-faded bottom-right" role="img" aria-label="Faded snowy pine branch with pinecones and red berries, with thin looping line ornaments"></div>
      <div class="brand-lockup">
        <div class="brand-dot"></div>
        <div class="brand-name">Dova<br>Lenthe</div>
      </div>
    </section>

    <section class="panel panel-cover">
      <div class="cover-field">
        <div class="wreath" role="img" aria-label="Snowy pine wreath with twigs, pinecones and red berries around an orange disc"></div>
      </div>
      <div class="greeting">
        <p class="greeting-year">2025</p>
        <p class="greeting-lead">Wishing you a happy</p>
        <h1 class="greeting-merry">MERRY</h1>
        <p class="greeting-christmas">CHRISTMAS</p>
      </div>
    </section>
  </main>
</body>
</html>
```